CEO of company needs clear business card that stands out from the rest

I need a clear business card (standard credit card size) for the CEO/Founder of our company...Brightfield Counseling. We would like to see designs that use our logo colors, which are khaki, chocolate brown, and gray. The card should be an edgy design, maybe where half the card is transparent with curves on the card, or a textured card where the logo is transparent, I don't care much for white cards. The final design should communicate a funky, edgy, and modern look, as well as stand out to have the "WOW" factor. The information we need on the card would be Name, Title, Toll free number, Phone Number, address, email address, and website.

*PLEASE SEND FRONT AND BACK OF CARDS

Card is two sided front and back please give us your front and back designs

The card should be an edgy design, maybe where half the card is transparent with curves on the card, or a textured card where the logo is transparent, I don't care much for white cards. The final design should communicate a funky, edgy, and modern look, as well as stand out to have the "WOW" factor.

Please follow these guidelines for the card

SPECS (card):

2.125 (h) x 3.375 (w) card size after cut

2.375 (h) x 3.625 (w) card with bleed

300 dpi

cmyk

1/8 bleed

allow 1/8 border for live area

I will also attached the pdf for the information listed above which includes a diagram of the card

 

All the cards need to have rounded edges

I just updated a card as an example of how you can use different fonts on a single business card, look how the name is written in script, so what I am saying is make this a card you will be proud to design and put it in your portfolio 

Reason: this race is really close and I am working with 2 designers to fine tune their designs and the weekend is slowing us down

• Our Logo
MUST HAVE PARTS OF CARD THAT ARE TRANSPARENT. See ideas that are attached.
Card is two sided front and back
• The final design should communicate a funky, edgy, and modern look, as well as stand out to have the "WOW" factor. The information we need on the card would be Name, Title, Toll free number, Phone Number, address, email address, and website.

```html
<!DOCTYPE html>
<html lang="en">
<head>
<meta charset="utf-8">
<title>Brightfield Counseling – Business Card Front and Back</title>
<link rel="stylesheet" href="https://fonts.googleapis.com/css2?family=Exo+2:wght@400;500&family=Quicksand:wght@400;500&display=swap">
<style>
  :root {
    --stage: #2f2f30;
    --band-khaki: #8c6026;
    --band-chocolate: #6a461c;
    --band-stripe: #a9927a;
    --card-gray: #3d3d3e;
    --card-gray-light: #5a5a59;
    --back-gray: #4a4a49;
    --back-gray-light: #6a6966;
    --text-brown: #4a3014;
    --text-khaki: #b8905e;
    --text-khaki-light: #c49a5f;
    --text-silver: #9a9ca0;
    --brand-dark: #1f1c19;
  }
  * { margin: 0; padding: 0; box-sizing: border-box; }
  html, body {
    width: 1200px;
    height: 1200px;
    overflow: hidden;
    background: var(--stage);
  }
  .sheet {
    position: relative;
    width: 1200px;
    height: 1200px;
  }
  .card {
    position: absolute;
    left: 210px;
    width: 818px;
    height: 480px;
    border-radius: 18px;
    overflow: hidden;
    box-shadow: 0 0 0 2px rgba(255,255,255,0.12);
  }
  .card--front {
    top: 74px;
    background: linear-gradient(160deg, var(--card-gray) 40%, var(--card-gray-light) 100%);
  }
  .card--back {
    top: 610px;
    background: linear-gradient(170deg, var(--back-gray) 0%, var(--back-gray-light) 100%);
  }
  .card__bands {
    position: absolute;
    inset: 0;
    width: 818px;
    height: 480px;
  }
  .toll-free {
    position: absolute;
    top: 22px;
    right: 38px;
    font: 400 18px "Exo 2", sans-serif;
    color: var(--text-brown);
  }
  .brand {
    position: absolute;
    display: flex;
    align-items: center;
    gap: 18px;
    font-family: "Quicksand", sans-serif;
    font-weight: 500;
    color: var(--brand-dark);
    white-space: nowrap;
  }
  .brand__dot {
    border-radius: 50%;
    background: var(--brand-dark);
    flex: none;
  }
  .card--front .brand {
    left: 84px;
    top: 72px;
    font-size: 46px;
  }
  .card--front .brand__dot { width: 44px; height: 44px; }
  .card--back .brand {
    left: 50%;
    top: 200px;
    transform: translateX(-50%);
    font-size: 54px;
  }
  .card--back .brand__dot { width: 52px; height: 52px; }
  .holder {
    position: absolute;
    left: 34px;
    top: 330px;
    width: 268px;
    font-family: "Quicksand", sans-serif;
    color: var(--text-silver);
  }
  .holder__name {
    font-size: 30px;
    font-weight: 400;
    white-space: nowrap;
  }
  .holder__title {
    margin-top: 10px;
    text-align: right;
    font: 400 16px "Exo 2", sans-serif;
  }
  .website {
    position: absolute;
    left: 50px;
    top: 436px;
    font: 400 17px "Exo 2", sans-serif;
    color: var(--text-silver);
  }
  .contact {
    position: absolute;
    right: 30px;
    top: 280px;
    text-align: right;
    font: 500 17px "Exo 2", sans-serif;
    color: var(--text-khaki);
    line-height: 36px;
  }
  .contact__gap { height: 18px; }
  .email {
    position: absolute;
    right: 30px;
    top: 436px;
    font: 400 17px "Exo 2", sans-serif;
    color: var(--text-khaki-light);
  }
</style>
</head>
<body>
<main class="sheet">

  <section class="card card--front" aria-label="Card front">
    <svg class="card__bands" viewBox="0 0 818 480" aria-hidden="true">
      <defs>
        <linearGradient id="band-fill" x1="0" y1="0" x2="1" y2="1">
          <stop offset="0" stop-color="var(--band-khaki)"/>
          <stop offset="1" stop-color="var(--band-chocolate)"/>
        </linearGradient>
      </defs>
      <path d="M0,166 C80,215 200,252 330,252 C500,252 680,215 818,160 L818,180 C680,238 500,274 330,274 C200,274 80,240 0,192 Z" fill="var(--band-stripe)" opacity="0.75"/>
      <path d="M0,0 H818 V160 C680,212 500,244 330,244 C200,244 80,210 0,160 Z" fill="url(#band-fill)"/>
    </svg>

    <p class="toll-free">Toll Free: 1-855-555-0142</p>

    <div class="brand">
      <span class="brand__dot"></span>
      <span class="brand__name">Brightfield Counseling</span>
    </div>

    <div class="holder">
      <p class="holder__name">Darren Whitcombe</p>
      <p class="holder__title">Founder / CEO</p>
    </div>

    <address class="contact">
      <p>4870 Harlow Ridge Dr. N.W. Suite 210</p>
      <p>Ashbury GA 30199</p>
      <div class="contact__gap"></div>
      <p>Phone : 404.555.0187</p>
      <p>Fax : 678.555.0133</p>
    </address>

    <p class="website">www.brightfieldcounseling.com</p>
    <p class="email">dwhitcombe@brightfieldcounseling.com</p>
  </section>

  <section class="card card--back" aria-label="Card back">
    <div class="brand">
      <span class="brand__dot"></span>
      <span class="brand__name">Brightfield Counseling</span>
    </div>
  </section>

</main>
</body>
</html>
```